Valdoro Mixers Agricultural Magazine Ad

We are placing an ad for our industrial mixer in an agricultural magazine. We need to create an ad for our "Fluidized Bed Mixers" showing the diversity of our product in the Agricultural Industry. Diversity includes mixing of fertilizers, seeds, & soil, to mixing of grains, greens, & hemp that was harvested. Below is the editorial that will be adjacent to the ad. I have also included images of the mixer as well as our logo. The ad area is Type area: 285mm x 200mm
Trim: 297mm x 210mm
------Editorial-----
In the past few years the agricultural industry has changed. From corn, soy, & fruits, to the newly added hemp & cannabis, the industry has grown. As the industry has grown, so has the technology that supports the industry, from software & hardware to tractors, watering devices, and even mixers.
From custom mixing & blending soils, fertilizers, & seeds, to mixing grains, greens, & beans, the need to increase productivity & decrease labor has also grown. Mixing has become an area that has had the need to drastically change as the ability to rapidly mix products that can be organic, natural, or synthetic has increased to support agriculture. The mixer that is on the rise is the Twin Paddle Mixer, also known as the Fluidized Bed Mixer. The Twin Paddle Mixer / Fluidized Bed Mixer is a high speed mixer that rapidly mixes products of different sizes & densities. It is unlike other mixers as it mixes in the air instead of the mixer's trough as with others such as Ribbon Mixers. The paddles make contact with the product and "fling" it into the air with enough velocity it breaks gravity, causing a "zero gravity" mixing. This is why particle size or density does not affect mixing. After mixing in the air the products fall back into the trough and the twin paddles keep them in motion, circulating, and repeat the mixing cycle. The process is completed very quickly, especially compared to other mixers, often cutting the time in half, or more. The speed at which products are mixed are also severely increased, decreasing labor intensity & increasing production.
There are also several option that can be engineered into the Twin Paddle Mixers / Fluidized Bed Mixers, such as adding / dosing or additives & fluids to products. The largest area we see this in is fertilizers & soils. The speed at which products are mixed are also severely increased, decreasing labor intensity & increasing production. The ability to rapidly mix while also adding nutrients or fortifying quickly is another reason the Twin Paddle Mixer / Fluidized Bed Mixer is chosen over others.
Another advantage of the Twin Paddle Mixer / Fluidized Bed Mixer in the agricultural industry is the way the mixer discharges afterwards. The bottom of the mixer is designed with twin rectangular doors that span the entire length of the mixing trough, these are known as "bombay doors". These doors are perfect for unloading directly into dump trailers. Whereas a normal mixer may need to be emptied into an auger conveyor to fill, the Twin Paddle Mixers / Fluidized Bed Mixers can be mounted on an elevated platform, allowing for trailers to be directly placed underneath of it and emptying of product can be completed in under 2 minutes. This is unique to this type of mixer over others.
As you can see the Twin Paddle Mixers / Fluidized Bed Mixers serve the industry better than any other mixer and Valdoro understands all the aspects of the agricultural industry, from fertilizers to seeds, soil to crops, & even harvesting. Increase production, decrease labor stress, & increase profits with Valdoro & the Valdoro line of mixers.
Pictures: Pictures attached should include one main picture of unit, a smaller picture of the internal paddles (maybe in a circular bubble), but should focus on the diverse areas of the industry we serve
Target Market(s)
Agricultural Industry from fertilizer manufacturers to farmers, from seed sellers to hemp growers
Industry/Entity Type
Agriculture
Requirements
Must have
- Valdoro logo
Incorporate somehow all the areas we serve the industry from

```html
<!DOCTYPE html>
<html lang="en">
<head>
<meta charset="utf-8">
<title>Valdoro Fluidized Bed Mixers – Agricultural Ad</title>
<link rel="stylesheet" href="https://fonts.googleapis.com/css2?family=Roboto:wght@300;700&display=swap">
<style>
  :root {
    --backdrop: #d4d4d4;
    --page: #eef0f1;
    --ink: #1f1f1f;
    --brand-red: #d22630;
    --brand-blue: #1a6fb5;
    --brand-navy: #1c3f8a;
    --frame: #ffffff;
  }
  * { margin: 0; padding: 0; box-sizing: border-box; }
  html, body { width: 1200px; height: 886px; overflow: hidden; background: var(--backdrop); }
  .canvas { position: relative; width: 1200px; height: 886px; }
  .ad {
    position: absolute; left: 87px; top: 77px; width: 1007px; height: 710px;
    background: var(--page); overflow: hidden;
  }
  .ad-art { position: absolute; inset: 0; }
  .editorial {
    position: absolute; left: 35px; top: 42px;
    font-family: "Roboto", Arial, sans-serif; font-weight: 300;
    font-size: 11.6px; line-height: 13.1px; color: var(--ink);
  }
  .editorial p { margin-bottom: 13.1px; }
  .editorial .narrow { width: 462px; }
  .editorial .wide { width: 575px; }
  .editorial .mid { width: 505px; }
  .brand {
    position: absolute; left: 50px; top: 618px;
    display: flex; align-items: center; gap: 8px;
    font-family: "Roboto", Arial, sans-serif; font-weight: 700;
    font-size: 34px; color: var(--brand-navy); letter-spacing: -0.5px;
  }
  .brand-dot { width: 24px; height: 24px; border-radius: 50%; background: var(--brand-red); }
  .inset {
    position: absolute; left: 561px; top: 486px; width: 227px; height: 184px;
    background: var(--frame); padding: 9px;
    transform: rotate(-3deg);
    box-shadow: 6px 8px 10px rgba(0,0,0,0.35);
  }
  .inset-photo {
    width: 100%; height: 100%;
    background: linear-gradient(135deg, #d8d8d6 0%, #8e8f8c 30%, #c9c8c3 50%, #5f605c 72%, #b5b3ad 100%);
  }
  .base-bar { position: absolute; left: 0; bottom: 0; height: 11px; width: 1007px; display: flex; }
  .base-bar .red { width: 502px; background: var(--brand-red); }
  .base-bar .blue { width: 258px; background: var(--brand-blue); }
</style>
</head>
<body>
<div class="canvas">
  <section class="ad">
    <svg class="ad-art" width="1007" height="710" viewBox="0 0 1007 710">
      <defs>
        <linearGradient id="field" x1="0" y1="0" x2="1" y2="1">
          <stop offset="0" stop-color="#3b5a3a"/>
          <stop offset="0.35" stop-color="#556d35"/>
          <stop offset="0.55" stop-color="#8a7a52"/>
          <stop offset="0.75" stop-color="#4f6a2e"/>
          <stop offset="1" stop-color="#2f4a22"/>
        </linearGradient>
      </defs>
      <g fill="#e3e6e8">
        <polygon points="0,0 180,0 60,160"/>
        <polygon points="240,120 420,60 360,300"/>
        <polygon points="0,380 160,300 120,520"/>
        <polygon points="300,520 520,420 460,700 260,700"/>
      </g>
      <g fill="#f6f7f8">
        <polygon points="120,200 300,260 180,420"/>
        <polygon points="420,300 560,240 540,460"/>
      </g>
      <polygon role="img" aria-label="Aerial photo of a tractor working a green crop field, dust trailing behind"
               points="489,0 1007,0 1007,699 735,699" fill="url(#field)"/>
      <polygon points="489,0 524,0 568,170 540,130" fill="var(--brand-blue)"/>
      <polygon points="829,71 1007,0 1007,420 889,90" fill="var(--brand-red)" opacity="0.85"/>
      <polygon points="895,0 1007,0 1007,45" fill="#e8404a" opacity="0.9"/>
    </svg>

    <div class="editorial">
      <p class="narrow">In the past few years the agricultural industry has changed. From corn, soy, &amp; fruits, to the newly added hemp &amp; cannabis, the industry has grown. As the industry has grown, so has the technology that supports the industry, from software &amp; hardware to tractors, watering devices, and even mixers.</p>
      <p class="narrow">From custom mixing &amp; blending soils, fertilizers, &amp; seeds, to mixing grains, greens, &amp; beans, the need to increase productivity &amp; decrease labor has also grown. Mixing has become an area that has had the need to drastically change as the ability to rapidly mix products that can be organic, natural, or synthetic has increased to support agriculture. The mixer that is on the rise is the Twin Paddle Mixer, also known as the Fluidized Bed Mixer. The Twin Paddle Mixer / Fluidized Bed Mixer is a high speed mixer that rapidly mixes products of different sizes &amp; densities. It is unlike other mixers as it mixes in the air instead of the mixer's trough as with others such as Ribbon Mixers. The paddles make contact with the product and "fling" it into the air with enough velocity it breaks gravity, causing a "zero gravity" mixing. This is why particle size or density does not affect mixing. After mixing in the air the products fall back into the trough and the twin paddles keep them in motion, circulating, and repeat the mixing cycle. The process is completed very quickly, especially compared to other mixers, often cutting the time in half, or more. The speed at which products are mixed are also severely increased, decreasing labor intensity &amp; increasing production.</p>
      <p class="wide">There are also several option that can be engineered into the Twin Paddle Mixers / Fluidized Bed Mixers, such as adding / dosing or additives &amp; fluids to products. The largest area we see this in is fertilizers &amp; soils. The speed at which products are mixed are also severely increased, decreasing labor intensity &amp; increasing production. The ability to rapidly mix while also adding nutrients or fortifying quickly is another reason the Twin Paddle Mixer / Fluidized Bed Mixer is chosen over others.</p>
      <p class="wide">Another advantage of the Twin Paddle Mixer / Fluidized Bed Mixer in the agricultural industry is the way the mixer discharges afterwards. The bottom of the mixer is designed with twin rectangular doors that span the entire length of the mixing trough, these are known as "bombay doors". These doors are perfect for unloading directly into dump trailers. Whereas a normal mixer may need to be emptied into an auger conveyor to fill, the Twin Paddle Mixers / Fluidized Bed Mixers can be mounted on an elevated platform, allowing for trailers to be directly placed underneath of it and emptying of product can be completed in under 2 minutes. This is unique to this type of mixer over others.</p>
      <p class="mid">As you can see the Twin Paddle Mixers / Fluidized Bed Mixers serve the industry better than any other mixer and Valdoro understands all the aspects of the agricultural industry, from fertilizers to seeds, soil to crops, &amp; even harvesting. Increase production, decrease labor stress, &amp; increase profits with Valdoro &amp; the Valdoro line of mixers.</p>
    </div>

    <div class="brand"><span class="brand-dot"></span>Valdoro</div>

    <figure class="inset">
      <div class="inset-photo" role="img" aria-label="Close-up of the stainless steel twin paddles inside the mixer trough"></div>
    </figure>

    <div class="base-bar"><span class="red"></span><span class="blue"></span></div>
  </section>
</div>
</body>
</html>
```